Modern corporate energy/fuel business need business card design

Business card required for company founder. Korvan Specialised Energy is a Australian based modern energy/fuel provider. We offer specialised solutions to businesses using fossil fuels through renewable energy solutions.

I would like one side with specific information (name, address etc)

The other side to be bold, professional company name & logo. Striking.

Target Market(s)

B2B. Transport, mining, councils, environmentalist,

Industry/Entity Type

Petroleum

Contact Information for Business Card

Name; Peter Morrow
Position; Director
Email; pmorrow@korvanse.com.au
Address; PO Box 347, Penrith, NSW, 2751
Website; www.korvanse.com.au

Colors

Designer to choose colors to be used in the design.

Requirements
Must have
• Clean, easy to read, professional & strong theme
Should not have
• too many colours, busy layout,

```html
<!DOCTYPE html>
<html lang="en">
<head>
<meta charset="utf-8">
<title>Korvan Specialised Energy – Business Card</title>
<link href="https://fonts.googleapis.com/css2?family=Lato:wght@400;700&display=swap" rel="stylesheet">
<style>
  :root {
    --stage: #2c2c2c;
    --card-white: #ffffff;
    --brand-blue: #24557a;
    --brand-orange: #f47a20;
    --orange-light: #fb9a45;
    --text-dark: #222222;
    --rule: #9a9a9a;
  }
  html, body {
    margin: 0;
    padding: 0;
    width: 1200px;
    height: 1200px;
    overflow: hidden;
    background: var(--stage);
    font-family: "Lato", Arial, sans-serif;
  }
  .stage {
    position: relative;
    width: 1200px;
    height: 1200px;
  }
  .card {
    position: absolute;
    top: 310px;
    width: 364px;
    height: 594px;
    box-shadow: 2px 3px 6px rgba(0,0,0,0.6);
  }
  .card-front {
    left: 234px;
    background: var(--card-white);
    text-align: center;
  }
  .card-back {
    left: 627px;
    width: 369px;
    overflow: hidden;
  }
  .wordmark {
    position: absolute;
    top: 470px;
    left: 0;
    width: 100%;
    top: 160px;
    display: flex;
    align-items: center;
    justify-content: center;
    gap: 14px;
  }
  .wordmark-dot {
    width: 62px;
    height: 62px;
    border-radius: 50%;
    background: var(--brand-orange);
    flex: none;
  }
  .wordmark-text {
    color: var(--brand-blue);
    font-weight: 700;
    text-align: left;
    line-height: 1;
  }
  .wordmark-name {
    display: block;
    font-size: 40px;
    letter-spacing: 4px;
  }
  .wordmark-tagline {
    display: block;
    font-size: 10px;
    letter-spacing: 5.4px;
    margin-top: 8px;
  }
  .contact {
    position: absolute;
    left: 0;
    width: 100%;
    top: 372px;
  }
  .person-name {
    margin: 0;
    color: var(--brand-blue);
    font-weight: 700;
    font-size: 22px;
    letter-spacing: -0.3px;
    line-height: 26px;
  }
  .person-role {
    margin: 0;
    color: var(--brand-orange);
    font-size: 16px;
    line-height: 18px;
  }
  .rule {
    width: 186px;
    height: 1px;
    background: var(--rule);
    margin: 10px auto;
    border: 0;
  }
  .contact-line {
    margin: 0;
    font-size: 16px;
    line-height: 21px;
    color: var(--text-dark);
  }
  .contact-web { color: var(--brand-blue); }
  .contact-web .accent { color: var(--brand-orange); }
  .contact-address { margin-top: 14px; }
  .back-art {
    position: absolute;
    inset: 0;
  }
  .back-name {
    position: absolute;
    left: 0;
    width: 100%;
    top: 268px;
    text-align: center;
    color: var(--card-white);
    font-weight: 700;
    font-size: 48px;
    letter-spacing: 6px;
  }
</style>
</head>
<body>
<main class="stage">
  <section class="card card-front">
    <div class="wordmark">
      <span class="wordmark-dot" aria-hidden="true"></span>
      <span class="wordmark-text">
        <span class="wordmark-name">KORVAN</span>
        <span class="wordmark-tagline">SPECIALISED ENERGY</span>
      </span>
    </div>
    <div class="contact">
      <h1 class="person-name">PETER MORROW</h1>
      <p class="person-role">Director</p>
      <hr class="rule">
      <p class="contact-line">pmorrow@korvanse.com.au</p>
      <p class="contact-line contact-web">www.<span class="accent">korvanse</span>.com.au</p>
      <hr class="rule">
      <p class="contact-line contact-address">PO Box 347, Penrith NSW, 2751</p>
    </div>
  </section>

  <section class="card card-back">
    <svg class="back-art" width="369" height="594" viewBox="0 0 369 594" aria-hidden="true">
      <defs>
        <radialGradient id="orangeGlow" cx="0.1" cy="0.05" r="1">
          <stop offset="0" stop-color="#fb9d4c"/>
          <stop offset="1" stop-color="#ff6f12"/>
        </radialGradient>
      </defs>
      <rect width="369" height="594" fill="url(#orangeGlow)"/>
      <polygon points="0,360 369,262 369,594 0,594" fill="#24557a"/>
    </svg>
    <div class="back-name">KORVAN</div>
  </section>
</main>
</body>
</html>
```